Entertainment Brochure Needed

The design needs to include information related to apartment designs.

Brochure Design Brief:
We are requiring an 8 ½” x 11 tri-fold brochure for marketing purposes for our entertainment company to distribute to our current and potential customers. The brochure exhibits services offered by our company along with themed events (DJ Services, Karaoke, Movie Night, Casino Night), Photo Booth, and concession machines/stations (Slushy Machines, Popcorn Machines, and Cotton Candy Machines). We require photos to depict our various themed events, along with the services we offer. We require the center (inside) of the brochure to flow through the brochure. We are looking to produce eye-catching graphics and content for all the services we offer.
As well as good marketing techniques.
Company Colors:
Maroon ( same color as the logo)
White
Black
It's okay to add another color that will complement our company colors

Note: will provide all text and pictures for the design....
I have all the content and pictures already set for the designer that will give full design details to make the design job easier for the designer. I will upload all content details once I select a designer for the job.

Target Market(s)

Professional. Brochure will be gear towards professionals in the apartment industry such as property managers

Industry/Entity Type

Entertainment

Other font styles liked:
• Open with the font

Colors

Designer to choose colors to be used in the design.

Requirements
Must have
• Professional brochure.
Should not have
• • Use too many font styles • Shrink text too small

```html
<!DOCTYPE html>
<html lang="en">
<head>
<meta charset="utf-8">
<title>Nova Stage Entertainment – Tri-fold Brochure</title>
<link href="https://fonts.googleapis.com/css2?family=Montserrat:wght@400;500;600;700&display=swap" rel="stylesheet">
<style>
:root{
  --maroon:#8c1015;
  --red:#c8262c;
  --ink:#141414;
  --black:#0b0b0b;
  --white:#ffffff;
  --stage:#a4a7a9;
  --band:#c9cbcd;
}
*{box-sizing:border-box;margin:0;padding:0}
html,body{width:1200px;height:502px;overflow:hidden;background:var(--stage)}
body{font-family:"Montserrat",sans-serif;color:var(--ink);position:relative}
.spread{position:absolute;top:37px;width:554px;height:428px;display:flex;box-shadow:0 2px 6px rgba(0,0,0,.25)}
.spread--outside{left:37px}
.spread--inside{left:609px}
.panel{position:relative;width:185px;height:100%;background:var(--white);overflow:hidden}
.panel+.panel{border-left:1px solid #e4e4e4}
.photo{position:absolute;left:0;width:100%}
.icon{position:absolute;width:33px;height:33px;border-radius:50%;background:var(--maroon);display:flex;align-items:center;justify-content:center}
.icon svg{width:18px;height:18px}
.title{position:absolute;font-weight:600;font-size:12.2px;line-height:14px;color:var(--ink)}
.bullets{position:absolute;list-style:none;font-size:6.2px;line-height:11.2px}
.bullets li{padding-left:10px;position:relative}
.bullets li::before{content:"";position:absolute;left:0;top:3.8px;width:3.6px;height:3.6px;border-radius:50%;background:var(--maroon)}
.body-copy{font-size:6.3px;line-height:9.8px;text-align:center}
.web{position:absolute;bottom:28px;left:0;width:100%;text-align:center;font-size:6.6px;font-weight:600;display:flex;justify-content:center;align-items:center;gap:4px}
.web i{width:8px;height:8px;border-radius:50%;background:var(--red);display:inline-block}

/* outside panels */
.community .icon{left:76px;top:12px}
.community .title{top:51px;width:100%;text-align:center}
.community .body-copy{position:absolute;top:87px;left:6px;right:6px}
.community .photo{top:0;height:100%;clip-path:polygon(0 141px,100% 173px,100% 100%,0 100%);background:radial-gradient(circle at 60% 40%,#c79a6a 0,#5a3c3a 40%,#1c1620 80%)}
.community .band{position:absolute;left:0;width:100%;top:0;height:100%;clip-path:polygon(0 139px,100% 171px,100% 175px,0 143px);background:var(--band)}

.curate .photo{top:0;height:100%;clip-path:polygon(0 0,100% 0,100% 305px,0 337px);background:radial-gradient(circle at 40% 35%,#f2b36a 0,#b8571f 35%,#4b1a0c 70%,#1a0805 100%)}
.curate .band{position:absolute;left:0;top:0;width:100%;height:100%;clip-path:polygon(0 337px,100% 305px,100% 309px,0 341px);background:var(--band)}
.curate h2{position:absolute;top:349px;width:100%;text-align:center;color:var(--red);font-size:12.5px;font-weight:600;letter-spacing:.5px}
.curate p{position:absolute;top:368px;width:100%;text-align:center;font-size:8px;font-weight:500}

.cover{background:var(--black)}
.cover .headline{position:absolute;top:19px;width:100%;text-align:center;color:var(--red);font-size:12.8px;font-weight:600;line-height:13px;letter-spacing:.6px}
.cover .tagline{position:absolute;top:49px;width:100%;text-align:center;color:var(--white);font-size:7.2px;line-height:11px}
.cover .photo{top:0;height:100%;clip-path:polygon(0 106px,100% 82px,100% 305px,0 340px);background:radial-gradient(circle at 55% 35%,#e2462c 0,#9c1a12 40%,#3a0606 80%)}
.cover .white-base{position:absolute;left:0;top:0;width:100%;height:100%;background:var(--white);clip-path:polygon(0 340px,100% 305px,100% 100%,0 100%)}
.cover .band{position:absolute;left:0;top:0;width:100%;height:100%;clip-path:polygon(0 337px,100% 302px,100% 306px,0 341px);background:var(--band)}
.brand{position:absolute;top:346px;width:100%;display:flex;justify-content:center;align-items:center;gap:6px}
.brand-mark{width:12px;height:12px;border-radius:50%;background:var(--maroon)}
.brand-name{color:var(--maroon);font-weight:700;font-size:10px;line-height:12px;text-align:left}

/* inside panels */
.service .title{left:10px;top:20px}
.service .icon{right:10px;top:16px}
.service .bullets{left:10px;top:52px}
.service .title.lower{top:232px}
.service .icon.lower{top:228px}
.service .bullets.lower{top:264px}
.service .bullets.lower-3{top:279px}
.dj-photo{top:0;height:100%;clip-path:polygon(0 211px,100% 180px,100% 92px,0 124px);background:linear-gradient(120deg,#2a1a14 0,#7a3a1c 45%,#c06a2a 70%,#2a140c 100%)}
.live-photo{top:0;height:100%;clip-path:polygon(0 344px,100% 313px,100% 100%,0 100%);background:radial-gradient(circle at 30% 60%,#e39a3c 0,#6a3a1c 35%,#1a1410 75%)}
.booth-photo{top:0;height:100%;clip-path:polygon(0 134px,100% 106px,100% 243px,0 274px);background:linear-gradient(160deg,#5d7a3c 0,#3a4a2a 40%,#7a5a3a 70%,#d9d4c8 100%)}
.movie-photo{top:0;height:100%;clip-path:polygon(0 124px,100% 92px,100% 180px,0 211px);background:linear-gradient(180deg,#1a1c22 0,#4a4c52 40%,#2a2420 100%)}
.production-photo{top:0;height:100%;clip-path:polygon(0 347px,100% 316px,100% 100%,0 100%);background:radial-gradient(circle at 70% 50%,#3a7ad8 0,#1a3c8a 40%,#0a0e24 80%)}
.service .addons-icon{left:76px;right:auto;top:281px}
.service .addons-title{left:0;top:321px;width:100%;text-align:center}
.addons-copy{position:absolute;top:356px;left:8px;right:8px}
</style>
</head>
<body>

<section class="spread spread--outside">
  <article class="panel community">
    <div class="icon"><svg viewBox="0 0 20 20" fill="none" stroke="#fff" stroke-width="1.6"><circle cx="10" cy="5" r="2"/><path d="M10 8v5M4 8l6 3 6-3M6 17l4-4 4 4"/></svg></div>
    <h2 class="title">Community Event<br>Experiences</h2>
    <p class="body-copy">Bring your community together with unforgettable entertainment designed for all ages. From music and movies to interactive attractions, we create vibrant, engaging environments that keep guests coming back.</p>
    <div class="photo" role="img" aria-label="Residents celebrating at a festive party with confetti and drinks"></div>
    <div class="band"></div>
  </article>

  <article class="panel curate">
    <div class="photo" role="img" aria-label="Guests laughing and raising glasses with sparklers at a night event"></div>
    <div class="band"></div>
    <h2>LET'S CURATE</h2>
    <p>Your Next Event Experience</p>
    <div class="web"><i></i>www.novastageevents.com</div>
  </article>

  <article class="panel cover">
    <h1 class="headline">MORE THAN<br>ENTERTAINMENT</h1>
    <p class="tagline">An Experience Your Residents Will<br>Remember.</p>
    <div class="photo" role="img" aria-label="DJ with headphones performing under red stage lights"></div>
    <div class="white-base"></div>
    <div class="band"></div>
    <div class="brand"><span class="brand-mark"></span><span class="brand-name">NOVA STAGE<br>ENTERTAINMENT</span></div>
    <div class="web"><i></i>www.novastageevents.com</div>
  </article>
</section>

<section class="spread spread--inside">
  <article class="panel service">
    <h2 class="title">Interactive DJ +<br>Karaoke Experience</h2>
    <div class="icon"><svg viewBox="0 0 20 20" fill="none" stroke="#fff" stroke-width="1.6"><circle cx="10" cy="10" r="7"/><circle cx="10" cy="10" r="2"/></svg></div>
    <ul class="bullets"><li>Professional DJs &amp; MCs</li><li>Extensive song library</li><li>High-quality sound &amp; lighting</li><li>Crowd engagement &amp; hosting</li></ul>
    <div class="photo dj-photo" role="img" aria-label="DJ hands on turntable mixer"></div>
    <h2 class="title lower">Live Music<br>Experience</h2>
    <div class="icon lower"><svg viewBox="0 0 20 20" fill="none" stroke="#fff" stroke-width="1.6"><path d="M8 15V4l8-2v11"/><circle cx="6" cy="15" r="2"/><circle cx="14" cy="13" r="2"/></svg></div>
    <ul class="bullets lower"><li>Solo artists, duos, or full bands</li><li>Custom music selection</li><li>Stage, sound &amp; lighting options</li><li>Engaging, crowd-friendly performances</li></ul>
    <div class="photo live-photo" role="img" aria-label="Guitarist performing on stage with warm lights"></div>
  </article>

  <article class="panel service">
    <h2 class="title">Photo Booth<br>Entertainment</h2>
    <div class="icon"><svg viewBox="0 0 20 20" fill="none" stroke="#fff" stroke-width="1.6"><rect x="4" y="3" width="12" height="14"/><circle cx="10" cy="9" r="2.5"/></svg></div>
    <ul class="bullets"><li>High-resolution photos &amp; prints</li><li>Fun props &amp; custom backdrops</li><li>Instant digital sharing</li><li>Attendant included for seamless experience</li></ul>
    <div class="photo booth-photo" role="img" aria-label="Outdoor photo booth with curtains and props table"></div>
    <div class="icon addons-icon"><svg viewBox="0 0 20 20" fill="none" stroke="#fff" stroke-width="1.6"><rect x="4" y="6" width="9" height="10"/><circle cx="15" cy="14" r="3"/><path d="M15 12.5v3M13.5 14h3"/></svg></div>
    <h2 class="title addons-title">Signature Event<br>Add-Ons</h2>
    <p class="body-copy addons-copy">Enhance your event with crowd-favorite extras that bring fun, flavor, and excitement to every experience. Our add-ons are the perfect complement to any package.</p>
  </article>

  <article class="panel service">
    <h2 class="title">Ultimate Outdoor<br>Movie Experience</h2>
    <div class="icon"><svg viewBox="0 0 20 20" fill="none" stroke="#fff" stroke-width="1.6"><circle cx="7" cy="6" r="2.5"/><circle cx="13" cy="6" r="2.5"/><rect x="4" y="10" width="10" height="6"/><path d="M14 12l3-2v6l-3-2"/></svg></div>
    <ul class="bullets"><li>Large outdoor screens</li><li>High-quality projection &amp; sound</li><li>Professional setup &amp; breakdown</li><li>Perfect for all ages and occasions</li></ul>
    <div class="photo movie-photo" role="img" aria-label="Audience watching an outdoor movie screen at dusk"></div>
    <h2 class="title lower">Event Production:<br>Audio, Visual &amp;<br>Lighting</h2>
    <div class="icon lower"><svg viewBox="0 0 20 20" fill="none" stroke="#fff" stroke-width="1.6"><rect x="3" y="4" width="14" height="9"/><path d="M10 13v4M6 17h8"/></svg></div>
    <ul class="bullets lower-3"><li>High-quality sound systems</li><li>LED screens &amp; visual displays</li><li>Custom lighting design</li><li>Professional setup &amp; on-site support</li></ul>
    <div class="photo production-photo" role="img" aria-label="Technician at an audio visual control desk with blue screens"></div>
  </article>
</section>

</body>
</html>
```